Hi everyone,
Clear Path Homes is a business that renovates older houses into modern homes. I'm looking for a design that is clean and simple. It needs to show the client that renovating is a simple process. No more than 3 colours to be used thanks.

What I need:
1. Logo
2. Business card (one side)
3. Letter head (A4)

Looking forward to the designs!

Industry/Entity Type

Construction

Logo Text

Clear Path Homes

Font styles to use
Sans Serif

Requirements
Must have
• Trading name: Clear Path Homes
• Contact name: Daniel Whitcombe
• Email: danielwhitcombe@clearpathhomes.com.au
• Tel: 0412 758 204
• Clean and simple
Nice to have
• If design might include a few tools. eg Hammer, paint roller etc.
Should not have
• Complicated design

```html
<!DOCTYPE html>
<html lang="en">
<head>
<meta charset="utf-8">
<title>Clear Path Homes – Stationery</title>
<link rel="stylesheet" href="https://fonts.googleapis.com/css2?family=Crimson+Pro:wght@400;600&display=swap">
<style>
  :root {
    --yellow: #fdc843;
    --grey: #d4d4d4;
    --ink: #1e1e1e;
    --paper: #ffffff;
    --page-edge: #b9b9b9;
  }
  * { margin: 0; padding: 0; box-sizing: border-box; }
  html, body {
    width: 1200px; height: 903px; overflow: hidden;
    background: var(--paper);
    font-family: "Crimson Pro", "Times New Roman", serif;
    color: var(--ink);
  }
  .letterhead {
    position: absolute; left: 281px; top: 40px;
    width: 638px; height: 825px;
    background: var(--paper);
    border: 1px solid var(--page-edge);
    overflow: hidden;
  }
  .brand {
    position: absolute; display: flex; align-items: center; gap: 8px;
    font-size: 19px; white-space: nowrap;
  }
  .brand-mark { width: 12px; height: 12px; background: var(--yellow); }
  .letterhead-brand { left: 34px; top: 72px; }
  .letterhead-contact-name {
    position: absolute; right: 40px; top: 72px; font-size: 19px;
  }
  .header-rule {
    position: absolute; left: 0; right: 0; top: 103px;
    height: 2px; background: var(--yellow);
  }
  .section-label {
    position: absolute; font-weight: 600; font-size: 16px;
  }
  .label-card { left: 168px; top: 226px; }
  .label-logo { left: 382px; top: 542px; }

  .business-card {
    position: absolute; left: 126px; top: 275px;
    width: 372px; height: 228px;
    background: var(--paper);
    border: 1px solid #dcdcdc;
    overflow: hidden;
  }
  .business-card svg.card-band { position: absolute; left: 0; top: 0; }
  .card-brand { left: 50%; transform: translateX(-50%); top: 60px; font-size: 20px; }
  .card-name {
    position: absolute; left: 142px; top: 128px; font-size: 19px;
  }
  .contact-line {
    position: absolute; display: flex; align-items: center; gap: 5px;
    font-size: 16px; white-space: nowrap;
  }
  .card-phone { left: 142px; top: 152px; }
  .card-email { left: 14px; top: 192px; font-size: 17px; }
  .icon { width: 12px; height: 12px; flex: none; }

  .logo-brand { left: 372px; top: 610px; font-size: 19px; }

  .footer-band { position: absolute; left: 0; bottom: 0; }
  .footer-phone { left: 42px; top: 794px; }
  .footer-email { left: 274px; top: 792px; font-size: 17px; }
</style>
</head>
<body>
  <main class="letterhead">
    <div class="brand letterhead-brand"><span class="brand-mark"></span>Clear Path Homes</div>
    <div class="letterhead-contact-name">Daniel Whitcombe</div>
    <div class="header-rule"></div>

    <div class="section-label label-card">BusinessCard</div>
    <section class="business-card">
      <svg class="card-band" width="372" height="228" viewBox="0 0 372 228">
        <polygon points="0,172 140,115 372,125 372,228 0,228" fill="var(--grey)"/>
        <polygon points="0,180 140,122 372,132 372,228 0,228" fill="var(--yellow)"/>
      </svg>
      <div class="brand card-brand"><span class="brand-mark"></span>Clear Path Homes</div>
      <div class="card-name">Daniel Whitcombe</div>
      <div class="contact-line card-phone">
        <svg class="icon" viewBox="0 0 12 12"><path d="M2.5 1 L4.5 1 L5 3.5 L3.8 4.5 Q5 7 7.5 8.2 L8.5 7 L11 7.5 L11 9.5 Q10.5 11 9 11 Q1 10 1 3 Q1 1.5 2.5 1 Z" fill="#fff"/></svg>
        0412 758 204
      </div>
      <div class="contact-line card-email">
        <svg class="icon" viewBox="0 0 12 12"><rect x="0.75" y="2.25" width="10.5" height="7.5" fill="none" stroke="#fff" stroke-width="1.2"/><path d="M0.75 2.25 L6 6.5 L11.25 2.25" fill="none" stroke="#fff" stroke-width="1.2"/></svg>
        danielwhitcombe@clearpathhomes.com.au
      </div>
    </section>

    <div class="section-label label-logo">Logo</div>
    <div class="brand logo-brand"><span class="brand-mark"></span>Clear Path Homes</div>

    <svg class="footer-band" width="638" height="120" viewBox="0 0 638 120">
      <polygon points="0,83 235,0 638,82 638,120 0,120" fill="var(--grey)"/>
      <polygon points="0,90 235,7 638,89 638,120 0,120" fill="var(--yellow)"/>
    </svg>
    <div class="contact-line footer-phone">
      <svg class="icon" viewBox="0 0 12 12"><path d="M2.5 1 L4.5 1 L5 3.5 L3.8 4.5 Q5 7 7.5 8.2 L8.5 7 L11 7.5 L11 9.5 Q10.5 11 9 11 Q1 10 1 3 Q1 1.5 2.5 1 Z" fill="#fff"/></svg>
      0412 758 204
    </div>
    <div class="contact-line footer-email">
      <svg class="icon" viewBox="0 0 12 12"><rect x="0.75" y="2.25" width="10.5" height="7.5" fill="none" stroke="#fff" stroke-width="1.2"/><path d="M0.75 2.25 L6 6.5 L11.25 2.25" fill="none" stroke="#fff" stroke-width="1.2"/></svg>
      danielwhitcombe@clearpathhomes.com.au
    </div>
  </main>
</body>
</html>
```